Software Company Business Card

We are looking for a new design of our business card. The design will also be used in the rest of our branding and marketing materials as we want to keep it all uniform. We sell POS software to fine/luxury jewelers and also offer other business services as well to help the jeweler manage their business and need something more updated, technical and fresh, preferably more on the masculine side. We do not want any designs with gems in them but if possible would like to incorporate the circle and arrow in the logo into the design, but not a requirement if you can't make it work. I would like to see a variety of the mix. The colors need to remain our blue and orange and the logo can not change. The squiggly lines have been used as our corporate identity for over 20 years and its time to update. Our company name is PELK (Bright Ledger Counter Solutions).

Target Market(s)

High End Jewelers

Industry/Entity Type

Software

Contact Information for Business Card

Requirements
Must have
• Our logo and the colors must remain the same. Blue is #d95d39 and Orange is #0f5682.
Nice to have
• The circle and arrow incorporated but not a requirement.
Should not have
• Anything jewelry or gem related.

```html
<!DOCTYPE html>
<html lang="en">
<head>
<meta charset="utf-8">
<title>PELK Business Card</title>
<link rel="stylesheet" href="https://fonts.googleapis.com/css2?family=Public+Sans:wght@300;400;700;800&display=swap">
<style>
  :root {
    --brand-blue: #065684;
    --brand-orange: #d95d39;
    --card-white: #ffffff;
    --badge-gold: #e9d7ad;
    --badge-grey: #dfe5e3;
  }
  html, body {
    margin: 0;
    padding: 0;
    width: 1200px;
    height: 1200px;
    overflow: hidden;
    background: var(--brand-orange);
    font-family: "Public Sans", Arial, sans-serif;
  }
  .card {
    position: absolute;
    left: 262px;
    width: 676px;
    height: 396px;
    background: var(--card-white);
    overflow: hidden;
    box-shadow: 6px 8px 14px rgba(90, 30, 10, 0.35);
  }
  .card--front { top: 138px; }
  .card--back { top: 665px; }
  .side-band {
    position: absolute;
    left: 0; top: 0;
    width: 23px; height: 100%;
    background: var(--brand-blue);
  }
  .brand {
    position: absolute;
    display: flex;
    align-items: center;
    color: var(--brand-blue);
    font-weight: 800;
    letter-spacing: 0.5px;
  }
  .brand__dot {
    border-radius: 50%;
    background: var(--brand-orange);
  }
  .card--front .brand { left: 395px; top: 28px; font-size: 46px; gap: 18px; }
  .card--front .brand__dot { width: 50px; height: 50px; }
  .card--back .brand { left: 81px; top: 70px; font-size: 84px; gap: 24px; }
  .card--back .brand__dot { width: 82px; height: 82px; }

  .person { position: absolute; left: 47px; top: 92px; color: var(--brand-blue); }
  .person__name { margin: 0; font-size: 32px; font-weight: 700; line-height: 1.1; }
  .person__title { margin: 2px 0 0; font-size: 17px; font-weight: 300; }
  .accent-rule {
    position: absolute;
    left: 23px; top: 174px;
    width: 55px; height: 4px;
    background: var(--brand-orange);
  }
  .contact, .address {
    position: absolute;
    top: 194px;
    margin: 0;
    color: var(--brand-blue);
    font-size: 17px;
    font-weight: 300;
    line-height: 20.7px;
  }
  .contact { left: 47px; display: grid; grid-template-columns: 54px auto; }
  .contact dt, .contact dd { margin: 0; }
  .address { left: 321px; font-style: normal; }

  .partner-badge {
    position: absolute;
    border-radius: 4px;
  }
  .partner-badge--gold { background: var(--badge-gold); }
  .partner-badge--grey { background: var(--badge-grey); }
  .card--front .partner-badge--gold { left: 70px; top: 322px; width: 126px; height: 43px; }
  .card--front .partner-badge--grey { left: 232px; top: 323px; width: 179px; height: 43px; }
  .card--back .partner-badge--gold { left: 81px; top: 322px; width: 125px; height: 44px; }
  .card--back .partner-badge--grey { left: 243px; top: 322px; width: 179px; height: 44px; }

  .growth-arrows {
    position: absolute;
    left: 0; top: 0;
    width: 676px; height: 396px;
  }
  .growth-arrows path { fill: none; stroke-width: 16; stroke-linecap: round; stroke-linejoin: round; }
  .arrow--blue { stroke: var(--brand-blue); }
  .arrow--orange { stroke: var(--brand-orange); }
</style>
</head>
<body>

<section class="card card--front" aria-label="Business card front">
  <div class="side-band"></div>
  <div class="brand"><span class="brand__name">PELK</span><span class="brand__dot"></span></div>

  <div class="person">
    <h1 class="person__name">Daniel Whitcombe</h1>
    <p class="person__title">Director of Global Operations</p>
  </div>
  <div class="accent-rule"></div>

  <dl class="contact">
    <dt>Phone</dt><dd>: +1 555 014-2286</dd>
    <dt>Fax</dt><dd>: +1 555 014-7391</dd>
    <dt>Email</dt><dd>: daniel@pelkcounter.com</dd>
    <dt>Web</dt><dd>: www.pelkcounter.com</dd>
  </dl>
  <address class="address">
    1840 Meridian Parkway<br>
    Suite 310<br>
    Cedar Falls, NV 89100<br>
    USA
  </address>

  <div class="partner-badge partner-badge--gold" role="img" aria-label="Partner show badge"></div>
  <div class="partner-badge partner-badge--grey" role="img" aria-label="Industry society badge"></div>

  <svg class="growth-arrows" viewBox="0 0 676 396" aria-hidden="true">
    <path class="arrow--orange" d="M516 316 V410 M477 353 L516 314 L555 353"/>
    <path class="arrow--blue" d="M602 244 V410 M563 282 L602 242 L641 282"/>
  </svg>
</section>

<section class="card card--back" aria-label="Business card back">
  <div class="side-band"></div>
  <div class="brand"><span class="brand__name">PELK</span><span class="brand__dot"></span></div>

  <div class="partner-badge partner-badge--gold" role="img" aria-label="Partner show badge"></div>
  <div class="partner-badge partner-badge--grey" role="img" aria-label="Industry society badge"></div>

  <svg class="growth-arrows" viewBox="0 0 676 396" aria-hidden="true">
    <path class="arrow--orange" d="M516 233 V410 M477 270 L516 231 L555 270"/>
    <path class="arrow--blue" d="M602 162 V410 M563 199 L602 160 L641 199"/>
  </svg>
</section>

</body>
</html>
```